Modern Business Card Design Needed for Young Realtor

Information that is going on the card:Marvin Pold
Broker/Owner
555.210.3367
Marvin@MPoldRealty.com
www.MPoldRealty.com

Would also like to include my Instagram Handle somewhere. Probably on the back: the_queencity_realtorMy previous business card is attached, I like that one but would like an updated version and maybe a few design changes

Marvin Pold
Broker/Owner
555.210.3367
Marvin@MPoldRealty.com
www.MPoldRealty.com

• Would also like to include my Instagram Handle somewhere. Probably on the back: the_pinecrest_realtor
• Dorrance Hale or the DH (logo from the previous card.)

```html
<!DOCTYPE html>
<html lang="en">
<head>
<meta charset="utf-8">
<title>MPold Realty Business Card</title>
<link href="https://fonts.googleapis.com/css2?family=Mulish:wght@400;600;700&display=swap" rel="stylesheet">
<style>
  :root {
    --page-bg: #262626;
    --card-light: #ebebea;
    --brand-red: #9b1b29;
    --bar-gray: #4d4d4d;
    --text-dark: #3e3e3e;
    --text-mid: #555555;
    --back-ink: #eeeae8;
    --photo-top: #d9d9d8;
    --photo-bottom: #6f7072;
  }
  * { margin: 0; padding: 0; box-sizing: border-box; }
  html, body {
    width: 1200px; height: 896px; overflow: hidden;
    background: var(--page-bg);
    font-family: "Mulish", Arial, sans-serif;
  }
  .canvas { position: relative; width: 1200px; height: 896px; }

  .card {
    position: absolute; left: 353px; width: 486px; height: 278px; overflow: hidden;
  }
  .card-front { top: 160px; background: var(--card-light); }
  .card-back { top: 469px; background: var(--brand-red); }

  .edge-bar { position: absolute; left: 0; width: 7px; background: var(--bar-gray); }
  .edge-bar-top { top: 0; height: 124px; }
  .edge-bar-bottom { top: 173px; bottom: 0; }
  .edge-accent { position: absolute; left: 0; top: 128px; width: 12px; height: 42px; background: var(--brand-red); }

  .brand-name {
    position: absolute; left: 45px; top: 62px;
    font-size: 15px; font-weight: 600; letter-spacing: 3px;
    color: var(--brand-red); text-transform: uppercase; white-space: nowrap;
  }

  .agent-name {
    position: absolute; left: 44px; top: 129px;
    font-size: 16px; font-weight: 700; color: var(--brand-red);
  }
  .agent-title {
    position: absolute; left: 44px; top: 149px;
    font-size: 12.5px; color: var(--text-mid);
  }

  .contact-list { position: absolute; left: 45px; top: 182px; list-style: none; }
  .contact-list li {
    display: flex; align-items: center; height: 16.5px;
    font-size: 12px; color: var(--text-mid);
  }
  .contact-list svg { width: 10px; height: 10px; margin-right: 8px; flex: none; }

  .agent-photo {
    position: absolute; left: 245px; top: 18px; width: 241px; height: 260px;
    background: linear-gradient(180deg, var(--photo-top) 0%, #b7b3b0 45%, var(--photo-bottom) 100%);
  }

  .back-brand {
    position: absolute; left: 0; right: 0; top: 136px; text-align: center;
    font-size: 29px; font-weight: 600; letter-spacing: 7px;
    color: var(--back-ink); text-transform: uppercase;
  }
  .social-handle {
    position: absolute; left: 0; right: 0; top: 224px;
    display: flex; justify-content: center; align-items: center;
    font-size: 12.5px; color: var(--back-ink);
  }
  .social-handle .mark { width: 9px; height: 9px; background: var(--back-ink); margin-right: 6px; }
</style>
</head>
<body>
<div class="canvas">
  <section class="card card-front">
    <div class="edge-bar edge-bar-top"></div>
    <div class="edge-accent"></div>
    <div class="edge-bar edge-bar-bottom"></div>

    <div class="brand-name">MPold Realty</div>

    <h1 class="agent-name">Marvin Pold</h1>
    <p class="agent-title">Broker/Owner</p>

    <ul class="contact-list">
      <li>
        <svg viewBox="0 0 10 10"><path d="M2 0.8 L3.6 2.6 L2.8 3.6 Q4 5.9 6.3 7.1 L7.3 6.3 L9.2 7.9 L8 9.3 Q3.5 8.6 0.7 2 Z" fill="var(--brand-red)"/></svg>
        555.210.3367
      </li>
      <li>
        <svg viewBox="0 0 10 10"><rect x="0.6" y="2" width="8.8" height="6" fill="none" stroke="var(--brand-red)" stroke-width="1"/><path d="M0.6 2 L5 5.6 L9.4 2 M0.6 8 L4 4.8 M9.4 8 L6 4.8" fill="none" stroke="var(--brand-red)" stroke-width="0.9"/></svg>
        Marvin@MPoldRealty.com
      </li>
      <li>
        <svg viewBox="0 0 10 10"><circle cx="5" cy="5" r="4.3" fill="none" stroke="var(--brand-red)" stroke-width="1"/><ellipse cx="5" cy="5" rx="1.9" ry="4.3" fill="none" stroke="var(--brand-red)" stroke-width="0.8"/><path d="M0.7 5 H9.3 M1.3 3 H8.7 M1.3 7 H8.7" stroke="var(--brand-red)" stroke-width="0.7"/></svg>
        www.MPoldRealty.com
      </li>
    </ul>

    <div class="agent-photo" role="img" aria-label="Portrait photo of the agent in a gray blazer and white shirt"></div>
  </section>

  <section class="card card-back">
    <div class="back-brand">MPold Realty</div>
    <div class="social-handle"><span class="mark"></span>the_pinecrest_realtor</div>
  </section>
</div>
</body>
</html>
```